Soccer (Football) travel website

I need a responsive 1-page website design for a vacation/trip review website, plus a basic logo. The site's name is GlobeKickJourneys.com.

A site I have in mind is VoyagePanel.com:

https://www.voyagepanel.com/sailto/sailroutes.cfm?port=149&startDate=2019-08

Target Market(s)

Landing page used to attract people after they've clicked on an advertisement

Industry/Entity Type

Travel

Logo Text

GlobeKickJourneys.com

Number of Pages Required

1 page

Font styles to use
Sans Serif

Colors

Designer to choose colors to be used in the design.

Requirements
Must have
• A header that takes up very little vertical space.
• I've attached one file. This is what the content will consist of in the center of the site: a photo of a stadium with some description text below it.
Nice to have
• Needs to have a simple nav plus links for social media and newsletter

```html
<!DOCTYPE html>
<html lang="en">
<head>
<meta charset="utf-8">
<title>GlobeKickJourneys.com — Soccer Travel</title>
<link href="https://fonts.googleapis.com/css2?family=Roboto:wght@400;500;700;900&family=Permanent+Marker&display=swap" rel="stylesheet">
<style>
:root{
  --sidebar:#1d1b1f;
  --ink:#2b2b2b;
  --muted:#6d6d6d;
  --accent:#d8262f;
  --paper:#ffffff;
  --band:#e7e4e1;
  --block:#000000;
}
*{box-sizing:border-box;margin:0;padding:0}
html,body{width:1200px;height:3124px;overflow:hidden;background:var(--paper)}
body{position:relative;font-family:'Roboto',Arial,sans-serif;color:var(--ink)}
.sidebar{position:absolute;left:0;top:0;width:72px;height:3124px;background:var(--sidebar)}
.menu-icon{position:absolute;left:20px;top:18px}
.brand{position:absolute;left:14px;top:64px;width:44px;height:44px;border:3px solid #fff;border-radius:50%}
.brand-name{position:absolute;left:36px;top:330px;transform:translateX(-50%) rotate(-90deg);transform-origin:center;color:#fff;font-size:11px;font-weight:500;letter-spacing:1px;white-space:nowrap}
.side-link{position:absolute;left:36px;top:1000px;transform:translateX(-50%) rotate(-90deg);color:#fff;font-size:13px;font-weight:500;letter-spacing:2px;white-space:nowrap}
.hero{position:absolute;left:72px;top:0;width:1128px;height:620px;background:radial-gradient(ellipse at 60% 25%,#5a86c8 0%,#1d3170 35%,#0b1430 60%),#0b1430}
.hero-pitch{position:absolute;left:0;bottom:0;width:100%;height:250px;background:linear-gradient(180deg,#2f7a34 0%,#164d1c 100%)}
.hero-title{position:absolute;left:120px;top:150px;color:#fff;font-family:'Permanent Marker',cursive;font-size:82px;line-height:96px;transform:rotate(-4deg)}
.hero-title span{display:block;padding-left:150px}
.btn{position:absolute;display:flex;align-items:center;justify-content:center;font-size:13px;font-weight:500;letter-spacing:1.5px;border:1px solid #bdbdbd;background:#fff;color:var(--ink)}
.hero .btn{left:228px;top:440px;width:180px;height:44px;border:none}
.section-title{position:absolute;font-weight:700;font-size:34px;letter-spacing:2px;color:var(--ink)}
.copy{position:absolute;width:420px;font-size:13px;line-height:20px;color:var(--muted)}
.photo{position:absolute}
.dots{position:absolute;left:1156px;top:1000px;width:8px}
.dots i{display:block;width:6px;height:6px;border-radius:50%;background:var(--accent);margin-bottom:5px}
.featured{position:absolute;left:72px;top:1408px;width:1128px;height:644px;background:var(--band)}
.centered{position:absolute;left:72px;width:1128px;text-align:center;font-weight:700;font-size:32px;letter-spacing:2px}
.arrow{position:absolute}
.tour-meta{position:absolute;left:72px;top:1890px;width:1128px;text-align:center;font-size:26px;font-weight:700;letter-spacing:2px}
.tour-meta .value{color:var(--accent)}
.tour-meta .gap{display:inline-block;width:60px}
.block{position:absolute;background:var(--block)}
.tour-info{position:absolute;left:432px;font-size:18px;font-weight:700;line-height:46px;letter-spacing:1px}
.tour-info .value{color:var(--accent)}
</style>
</head>
<body>
<aside class="sidebar">
  <svg class="menu-icon" width="32" height="24" viewBox="0 0 32 24"><rect y="2" width="32" height="3" fill="#fff"/><rect y="11" width="32" height="3" fill="#fff"/><rect y="20" width="32" height="3" fill="#fff"/></svg>
  <div class="brand"></div>
  <div class="brand-name">GlobeKickJourneys.com</div>
  <div class="side-link">ABOUT US</div>
</aside>

<header class="hero" role="img" aria-label="Floodlit stadium with a player's foot resting on a soccer ball">
  <div class="hero-pitch"></div>
  <h1 class="hero-title">WANT TO WATCH<span>THIS CLOSE ?</span></h1>
  <a class="btn">JOIN US</a>
</header>

<section class="about">
  <h2 class="section-title" style="left:148px;top:716px">WHO WE ARE?</h2>
  <p class="copy" style="left:148px;top:782px">GlobeKickJourneys is a travel team that plans match trips for fans. We book seats, hotels and transfers so you can enjoy the game from the best spot in the stadium, and we guide you through each city along the way with care.</p>
  <div class="photo" style="left:640px;top:688px;width:320px;height:248px;background:radial-gradient(circle at 45% 50%,#ffe26a 0%,#f2b81a 45%,#c88a0c 100%)" role="img" aria-label="Fan holding a yellow smoke flare"></div>

  <div class="photo" style="left:152px;top:1000px;width:340px;height:280px;background:linear-gradient(180deg,#2a1a12 0%,#b4521c 55%,#f08a2a 72%,#3a1d10 100%)" role="img" aria-label="Silhouette of a person jumping at sunset"></div>
  <h2 class="section-title" style="left:640px;top:1042px">WHY TRAVEL WITH US?</h2>
  <p class="copy" style="left:640px;top:1104px">GlobeKickJourneys takes care of every detail of your trip. Our local guides know each stadium, each city and each fan zone, so your days are easy, your seats are close and your memories last long after the final whistle.</p>
  <a class="btn" style="left:728px;top:1292px;width:172px;height:48px">JOIN US</a>
  <div class="dots"><i></i><i></i></div>
</section>

<section class="featured"></section>
<h2 class="centered" style="top:1462px">OUR FEATURED TOURS</h2>
<svg class="arrow" style="left:160px;top:1650px" width="30" height="60" viewBox="0 0 30 60"><path d="M26 4 L6 30 L26 56" fill="none" stroke="var(--accent)" stroke-width="6"/></svg>
<div class="photo" style="left:236px;top:1520px;width:20px;height:312px;background:#6a8aa8"></div>
<div class="photo" style="left:260px;top:1520px;width:752px;height:312px;background:linear-gradient(180deg,#8fb8e0 0%,#c9d9ea 30%,#b52a30 48%,#d8333a 68%,#3f8a3a 80%,#2f7330 100%)" role="img" aria-label="Stadium stands with red seats and green pitch"></div>
<div class="photo" style="left:1016px;top:1520px;width:20px;height:312px;background:#6a8aa8"></div>
<svg class="arrow" style="left:1074px;top:1650px" width="30" height="60" viewBox="0 0 30 60"><path d="M4 4 L24 30 L4 56" fill="none" stroke="var(--ink)" stroke-width="6"/></svg>
<p class="tour-meta">PLACE: <span class="value">LIVERPOOL</span><span class="gap"></span>DATE: <span class="value">MARCH</span></p>
<a class="btn" style="left:552px;top:1944px;width:176px;height:48px">TRAVEL NOW</a>

<section class="tours">
  <h2 class="centered" style="top:2106px">PICK A TOUR NOW</h2>
  <div class="block" style="left:152px;top:2220px;width:248px;height:212px"></div>
  <div class="tour-info" style="top:2226px">PLACE: <span class="value">LIVERPOOL</span><br>DATE: <span class="value">MARCH</span><br>DURATION: <span class="value">3 WEEKS</span><br>PRICE: <span class="value">$2000</span></div>
  <div class="block" style="left:152px;top:2468px;width:248px;height:212px"></div>
  <div class="tour-info" style="top:2474px">PLACE: <span class="value">LIVERPOOL</span><br>DATE: <span class="value">MARCH</span><br>DURATION: <span class="value">3 WEEKS</span><br>PRICE: <span class="value">$2000</span></div>
  <div class="block" style="left:152px;top:2720px;width:248px;height:212px"></div>
  <div class="tour-info" style="top:2726px">PLACE: <span class="value">LIVERPOOL</span><br>DATE: <span class="value">MARCH</span><br>DURATION: <span class="value">3 WEEKS</span><br>PRICE: <span class="value">$2000</span></div>
  <div class="block" style="left:860px;top:2220px;width:188px;height:608px"></div>
</section>
</body>
</html>
```